Half Wrap Van Design for Solar Battery Company

We require a half van wraps design, for the KRT M45+ Van. The van colour is white.

We are a solar and battery installation company in Victoria. Our business name is Hollowmere Brightline Co.

We want to embody high quality, premium installations. I don't want it to look cheap, but elegant.

Also it must be unique and provide the onlookers an ability to quickly identify what work we do and how to easily contact us

Target Market(s)

Residential customers in Victoria

Industry/Entity Type

Solar battery industry

Colors
0054AA
0677BA
7BADD7
CADEEF
E8F1F8

Requirements
Must have
• Our corporate colours, look smart. High tech. Include solar panels or other nice graphics
Should not have
• Cheap looking low resolution images

```html
<!DOCTYPE html>
<html lang="en">
<head>
<meta charset="utf-8">
<title>Hollowmere Brightline Co – Half Wrap Concepts, KRT M45+</title>
<link rel="stylesheet" href="https://fonts.googleapis.com/css2?family=Montserrat:wght@600;700;800;900&display=swap">
<style>
  :root {
    --brand-deep: #0054AA;
    --brand-mid: #0677BA;
    --brand-light: #7BADD7;
    --brand-pale: #CADEEF;
    --brand-mist: #E8F1F8;
    --ink: #0b0d12;
    --van-white: #f4f5f7;
    --van-shade: #d9dce1;
    --tyre: #1d1f23;
    --rim: #aeb3ba;
    --backdrop: #eceef1;
  }
  html, body {
    margin: 0;
    padding: 0;
    width: 799px;
    height: 1200px;
    overflow: hidden;
    background: var(--backdrop);
    font-family: "Montserrat", sans-serif;
  }
  .concept-sheet {
    width: 799px;
    height: 1200px;
    display: flex;
    flex-direction: column;
  }
  .wrap-concept {
    display: block;
    width: 799px;
    height: 400px;
  }
  .shared-defs { position: absolute; width: 0; height: 0; }
  .tagline { font-weight: 900; fill: #ffffff; stroke: var(--ink); stroke-width: 1.2px; paint-order: stroke; letter-spacing: 0.5px; }
  .tagline-sub { font-weight: 800; fill: var(--brand-pale); letter-spacing: 0.5px; }
  .phone-number { font-weight: 800; fill: #ffffff; font-size: 19px; }
  .brand-name { font-weight: 800; fill: var(--brand-deep); }
  .web-address { font-weight: 700; fill: #ffffff; font-size: 10px; }
</style>
</head>
<body>
<svg class="shared-defs" aria-hidden="true">
  <defs>
    <clipPath id="van-clip">
      <path d="M90 125 Q95 107 125 107 L430 107 Q470 108 520 135 L600 185 Q690 203 718 232 Q732 258 730 298 L726 322 L80 322 Q74 300 77 268 L84 190 Z"/>
    </clipPath>
    <linearGradient id="solar-tone" x1="0" y1="0" x2="1" y2="1">
      <stop offset="0" stop-color="#7BADD7"/>
      <stop offset="0.5" stop-color="#CADEEF"/>
      <stop offset="1" stop-color="#0677BA"/>
    </linearGradient>
    <linearGradient id="band-tone" x1="0" y1="0" x2="1" y2="0">
      <stop offset="0" stop-color="#0054AA"/>
      <stop offset="1" stop-color="#0677BA"/>
    </linearGradient>
    <symbol id="van-wrap" viewBox="0 0 799 400">
      <!-- van body -->
      <path fill="var(--van-white)" stroke="var(--van-shade)" stroke-width="1.5" d="M90 125 Q95 107 125 107 L430 107 Q470 108 520 135 L600 185 Q690 203 718 232 Q732 258 730 298 L726 322 L80 322 Q74 300 77 268 L84 190 Z"/>
      <path class="side-window" fill="#2b3038" d="M452 124 L520 126 Q560 150 590 185 L452 190 Z"/>
      <line x1="438" y1="112" x2="438" y2="322" stroke="var(--van-shade)" stroke-width="1.2"/>
      <line x1="565" y1="190" x2="565" y2="322" stroke="var(--van-shade)" stroke-width="1.2"/>
      <g clip-path="url(#van-clip)">
        <!-- solar panel field -->
        <rect x="70" y="100" width="320" height="80" fill="url(#solar-tone)" role="img" aria-label="Solar panel array graphic in brand blues"/>
        <!-- blue sweep behind diagonals -->
        <polygon points="300,100 430,100 362,180 232,180" fill="var(--brand-mid)" opacity="0.85"/>
        <polygon points="372,100 400,100 330,180 302,180" fill="var(--ink)"/>
        <polygon points="405,100 420,100 350,180 335,180" fill="var(--brand-deep)"/>
        <!-- phone band -->
        <polygon points="70,178 420,178 410,204 70,204" fill="var(--ink)"/>
        <!-- right chevron -->
        <polygon points="350,180 455,180 485,200 485,230 390,322 330,322 440,228 440,210" fill="var(--brand-light)"/>
        <polygon points="420,180 445,180 478,205 478,228 388,322 366,322 462,226 462,206" fill="var(--brand-mid)"/>
        <polygon points="395,204 418,204 455,228 358,322 336,322 432,230" fill="var(--ink)"/>
        <!-- lower band -->
        <polygon points="70,262 400,262 346,322 70,322" fill="url(#band-tone)"/>
        <polygon points="70,262 410,262 400,272 70,272" fill="var(--ink)"/>
        <polygon points="270,272 400,272 372,292 252,292" fill="var(--ink)"/>
        <polygon points="120,296 330,296 310,322 120,322" fill="var(--brand-light)" opacity="0.6"/>
      </g>
      <!-- wheels -->
      <circle cx="200" cy="318" r="52" fill="var(--backdrop)"/>
      <circle cx="640" cy="318" r="52" fill="var(--backdrop)"/>
      <circle cx="200" cy="318" r="46" fill="var(--tyre)"/>
      <circle cx="640" cy="318" r="46" fill="var(--tyre)"/>
      <circle cx="200" cy="318" r="28" fill="var(--rim)"/>
      <circle cx="640" cy="318" r="28" fill="var(--rim)"/>
      <circle cx="200" cy="318" r="6" fill="#6b7078"/>
      <circle cx="640" cy="318" r="6" fill="#6b7078"/>
      <!-- tail light -->
      <rect x="86" y="190" width="48" height="20" rx="5" fill="#c3272f"/>
      <!-- phone -->
      <path d="M160 184 q-4 8 0 14 l3 -2 q-3 -4 0 -10 z" fill="var(--brand-light)"/>
      <text class="phone-number" x="178" y="198">1300 555 019</text>
      <!-- brand name -->
      <text class="brand-name" x="148" y="236" font-size="29">HOLLOWMERE</text>
      <line x1="145" y1="252" x2="225" y2="252" stroke="var(--ink)" stroke-width="1.5"/>
      <text class="brand-name" x="232" y="257" font-size="14" letter-spacing="4">BRIGHTLINE CO</text>
      <line x1="378" y1="252" x2="430" y2="252" stroke="var(--ink)" stroke-width="1.5"/>
      <text class="web-address" x="290" y="285" transform="rotate(-3 290 285)">hollowmerebright.com.au</text>
    </symbol>
  </defs>
</svg>

<main class="concept-sheet">
  <svg class="wrap-concept" viewBox="0 0 799 400" role="group" aria-label="Wrap concept one">
    <use href="#van-wrap"/>
    <text class="tagline" x="182" y="140" font-size="19" transform="rotate(3 182 140)">SOLAR BATTERY</text>
    <rect x="218" y="148" width="120" height="22" rx="3" fill="var(--ink)" transform="rotate(3 218 148)"/>
    <text class="tagline-sub" x="236" y="165" font-size="15" fill="var(--brand-light)" transform="rotate(3 236 165)">SPECIALISTS</text>
  </svg>

  <svg class="wrap-concept" viewBox="0 0 799 400" role="group" aria-label="Wrap concept two">
    <use href="#van-wrap"/>
    <text class="tagline" x="165" y="138" font-size="19" transform="rotate(3 165 138)">SOLAR BATTERY</text>
    <rect x="168" y="145" width="176" height="22" rx="3" fill="var(--ink)" transform="rotate(3 168 145)"/>
    <circle cx="180" cy="153" r="5" fill="none" stroke="var(--brand-light)" stroke-width="1.6"/>
    <text class="tagline-sub" x="193" y="162" font-size="14" fill="#ffffff" letter-spacing="2" transform="rotate(3 193 162)">SPECIALISTS</text>
    <circle cx="334" cy="163" r="5" fill="none" stroke="var(--brand-light)" stroke-width="1.6"/>
  </svg>

  <svg class="wrap-concept" viewBox="0 0 799 400" role="group" aria-label="Wrap concept three">
    <use href="#van-wrap"/>
    <text class="tagline" x="162" y="137" font-size="19" transform="rotate(3 162 137)">SOLAR BATTERY</text>
    <rect x="218" y="146" width="128" height="22" rx="2" fill="var(--ink)" transform="rotate(3 218 146)"/>
    <text class="tagline-sub" x="226" y="163" font-size="15" fill="var(--brand-light)" transform="rotate(3 226 163)">SPECIALISTS</text>
  </svg>
</main>
</body>
</html>
```